Corvane Supplies Business Card

Professional business card that stand out to our potential customers. Front and back with clean modern design

Industry/Entity Type

Oil and gas

Contact Information for Business Card

Name, address, website , office phone and cell number

Requirements
Must have
• Editable files for each employee

```html
<!DOCTYPE html>
<html lang="en">
<head>
<meta charset="utf-8">
<title>Corvane Supplies Business Card</title>
<link rel="stylesheet" href="https://fonts.googleapis.com/css2?family=Poppins:wght@400;600&display=swap">
<style>
  :root {
    --red: #ec2127;
    --cyan: #12afd6;
    --ink: #333333;
    --paper: #ffffff;
    --stage: #eeeff2;
    --edge: #c9c9cc;
  }
  * { box-sizing: border-box; margin: 0; padding: 0; }
  html, body {
    width: 1163px; height: 1200px; overflow: hidden;
    background: var(--stage);
    font-family: "Poppins", Arial, sans-serif;
  }
  .sheet {
    width: 1163px; height: 1200px;
    display: flex; flex-direction: column; align-items: center; justify-content: center;
    gap: 70px;
  }
  .card {
    position: relative;
    width: 780px; height: 446px;
    overflow: hidden;
  }
  .card-front { background: var(--paper); border: 1px solid var(--edge); }
  .card-back { background: var(--red); display: flex; align-items: center; justify-content: center; }

  .holder { position: absolute; left: 0; top: 95px; width: 320px; }
  .holder-name {
    margin-left: 37px;
    color: var(--cyan); font-weight: 600; font-size: 35px; line-height: 1;
    letter-spacing: 0.2px; white-space: nowrap;
  }
  .holder-rule { display: flex; align-items: center; margin-top: 8px; }
  .holder-rule .rule { width: 310px; height: 1.5px; background: var(--ink); }
  .holder-title { margin-left: 8px; font-size: 22px; color: var(--ink); letter-spacing: 1px; line-height: 1; }

  .contact { position: absolute; left: 37px; top: 222px; list-style: none; color: var(--ink); font-size: 22px; line-height: 28px; letter-spacing: 0.8px; }
  .contact li { display: flex; align-items: flex-start; gap: 12px; }
  .contact li + li { margin-top: 3px; }
  .contact li.gap { margin-top: 18px; }
  .contact .icon { flex: none; width: 24px; height: 24px; margin-top: 3px; }

  .brand {
    position: absolute; left: 480px; top: 150px; width: 270px;
    display: flex; flex-direction: column; align-items: center; gap: 14px;
  }
  .brand-square { width: 70px; height: 70px; background: var(--red); }
  .brand-name { color: var(--red); font-weight: 600; font-size: 26px; letter-spacing: 0.5px; white-space: nowrap; }

  .footer-band { position: absolute; left: 0; bottom: 0; width: 780px; height: 38px; }

  .back-name { color: var(--paper); font-weight: 600; font-size: 46px; letter-spacing: 1px; }
</style>
</head>
<body>
<main class="sheet">
  <section class="card card-front" aria-label="Business card front">
    <div class="holder">
      <h1 class="holder-name">MAREN OSKETT</h1>
      <div class="holder-rule"><span class="rule"></span><span class="holder-title">CEO</span></div>
    </div>

    <ul class="contact">
      <li>
        <svg class="icon" viewBox="0 0 24 24" aria-hidden="true"><circle cx="12" cy="12" r="12" fill="var(--red)"/><path d="M12 5.5a4 4 0 0 0-4 4c0 3 4 8 4 8s4-5 4-8a4 4 0 0 0-4-4z" fill="#fff"/><circle cx="12" cy="9.5" r="1.5" fill="var(--red)"/></svg>
        <span>4120 Linden Ave<br>Odessa, TX 79761</span>
      </li>
      <li>
        <svg class="icon" viewBox="0 0 24 24" aria-hidden="true"><circle cx="12" cy="12" r="12" fill="var(--red)"/><path d="M8.2 6.5l2 2.2-1 1.4a8 8 0 0 0 4.7 4.7l1.4-1 2.2 2-1.2 1.7C11.5 17.3 6.7 12.5 6.5 7.7z" fill="#fff"/></svg>
        <span>432 5550 1947</span>
      </li>
      <li class="gap">
        <svg class="icon" viewBox="0 0 24 24" aria-hidden="true"><circle cx="12" cy="12" r="12" fill="var(--red)"/><rect x="6.5" y="8" width="11" height="8" fill="none" stroke="#fff" stroke-width="1.4"/><path d="M6.5 8l5.5 4.5L17.5 8" fill="none" stroke="#fff" stroke-width="1.4"/></svg>
        <span>maren@corvane.com</span>
      </li>
      <li>
        <svg class="icon" viewBox="0 0 24 24" aria-hidden="true"><circle cx="12" cy="12" r="12" fill="var(--red)"/><g fill="none" stroke="#fff" stroke-width="1.2"><circle cx="12" cy="12" r="5.5"/><ellipse cx="12" cy="12" rx="2.4" ry="5.5"/><path d="M6.5 12h11M7.3 9.2h9.4M7.3 14.8h9.4"/></g></svg>
        <span>www.corvane.com</span>
      </li>
    </ul>

    <div class="brand">
      <span class="brand-square" aria-hidden="true"></span>
      <span class="brand-name">CORVANE SUPPLIES</span>
    </div>

    <svg class="footer-band" viewBox="0 0 780 38" preserveAspectRatio="none" aria-hidden="true">
      <path d="M0 0H514C500 6 494 20 491 38H0Z" fill="var(--red)"/>
      <path d="M780 0H556C536 0 524 14 519 38H780Z" fill="var(--cyan)"/>
    </svg>
  </section>

  <section class="card card-back" aria-label="Business card back">
    <span class="back-name">CORVANE SUPPLIES</span>
  </section>
</main>
</body>
</html>
```